Ward Compass Business Card Design*

We need a business card design for our company Ward Compass. Our company is specialized in providing online consulting services regarding medical institutions, hospitals and doctors. We work with patients worldwide looking to choose between healthcare providers. We have a website you may use as a reference, where we list doctors and clinics worldwide. So we target Medical providers as well as patients worldwide.
Target Market(s)
Medical Providers and patients around the world
Industry/Entity Type
Medical
Contact Information for Business Card
Salma Derkaoui
CEO
+90 612 348 2071
info@wardcompass-example.com
www.wardcompass-example.com
14 Annakhil 3 H.R.B. Rabat, Morocco
Requirements
Must have
- Company logo/name on one full side, personal info and smaller logo and company name on the other side.
Nice to have
- Smart and elegant design

```html
<!DOCTYPE html>
<html lang="en">
<head>
<meta charset="utf-8">
<title>Ward Compass – Business Card</title>
<link rel="stylesheet" href="https://fonts.googleapis.com/css2?family=Montserrat:wght@400;500;700&family=Quicksand:wght@500&display=swap">
<style>
  :root {
    --backdrop: #e4e0d8;
    --paper: #f4f4f3;
    --navy: #0f3a63;
    --navy-deep: #0b2a48;
    --grey: #858586;
    --grey-deep: #58585a;
    --green: #8dc63f;
    --ink: #232323;
    --dots: #e2e2e3;
  }
  * { margin: 0; padding: 0; box-sizing: border-box; }
  html, body { width: 900px; height: 1200px; overflow: hidden; }
  body { background: var(--backdrop); position: relative; font-family: "Montserrat", sans-serif; }

  .card {
    position: absolute;
    background: var(--paper);
    border-radius: 18px;
    overflow: hidden;
    box-shadow: 0 6px 14px rgba(0,0,0,.18);
  }
  .card-front { left: 78px; top: 137px; width: 762px; height: 433px; }
  .card-back  { left: 76px; top: 630px; width: 767px; height: 436px; }
  .card svg.shapes { position: absolute; inset: 0; }

  /* front */
  .holder { position: absolute; right: 45px; top: 48px; text-align: right; color: #fff; }
  .holder-name { font-weight: 700; font-size: 34px; letter-spacing: .5px; line-height: 1; }
  .holder-name .surname { color: var(--green); }
  .holder-role { font-weight: 500; font-size: 29px; margin-top: 10px; line-height: 1; }

  .contacts { position: absolute; right: 44px; top: 216px; list-style: none; }
  .contacts li {
    display: flex; align-items: center; justify-content: flex-end;
    height: 34px; margin-bottom: 15px;
    font-family: "Quicksand", sans-serif; font-weight: 500; font-size: 21px; color: var(--ink);
    letter-spacing: .4px;
  }
  .contacts .icon { width: 34px; height: 34px; margin-left: 16px; flex: none; }

  .front-brand { position: absolute; left: 58px; top: 138px; color: var(--navy); }
  .front-brand .mark { width: 78px; height: 78px; border-radius: 50%; background: var(--navy); }
  .front-brand .brand-name { font-weight: 700; font-size: 40px; line-height: 1.05; margin-top: 18px; letter-spacing: 1px; }

  .dot-band {
    position: absolute; left: 0; right: 0; bottom: 0; height: 52px;
    background: linear-gradient(var(--paper), var(--dots));
  }

  /* back */
  .back-brand { position: absolute; left: 104px; top: 148px; display: flex; align-items: center; }
  .back-brand .mark { width: 110px; height: 110px; border-radius: 50%; background: var(--navy); }
  .back-brand .brand-name { margin-left: 30px; font-weight: 700; font-size: 50px; color: var(--navy); letter-spacing: 1px; }
</style>
</head>
<body>

<section class="card card-front" aria-label="Business card, personal side">
  <svg class="shapes" width="762" height="433" viewBox="0 0 762 433">
    <path fill="var(--navy-deep)" d="M0,0 H762 V165 C560,180 300,130 0,18 Z"/>
    <path fill="var(--navy)" d="M30,0 H762 V150 C560,162 320,110 30,0 Z"/>
  </svg>

  <div class="holder">
    <p class="holder-name">SALMA <span class="surname">DERKAOUI</span></p>
    <p class="holder-role">CEO</p>
  </div>

  <div class="front-brand">
    <div class="mark"></div>
    <p class="brand-name">WARD<br>COMPASS</p>
  </div>

  <ul class="contacts">
    <li>+90 612 348 2071
      <svg class="icon" viewBox="0 0 34 34" aria-hidden="true"><circle cx="17" cy="17" r="17" fill="var(--navy)"/><path fill="#fff" d="M9 14c0-3 4-4 8-4s8 1 8 4v2h-4v-2c-1-1-7-1-8 0v2H9z M11 18h12l1 6H10z"/></svg>
    </li>
    <li>info@wardcompass-example.com
      <svg class="icon" viewBox="0 0 34 34" aria-hidden="true"><circle cx="17" cy="17" r="17" fill="var(--navy)"/><rect x="9" y="11" width="16" height="12" rx="1.5" fill="#fff"/><path d="M9.5 12 17 18l7.5-6" fill="none" stroke="var(--navy)" stroke-width="1.6"/></svg>
    </li>
    <li>www.wardcompass-example.com
      <svg class="icon" viewBox="0 0 34 34" aria-hidden="true"><circle cx="17" cy="17" r="17" fill="var(--navy)"/><g fill="none" stroke="#fff" stroke-width="1.6"><circle cx="17" cy="17" r="8"/><ellipse cx="17" cy="17" rx="3.5" ry="8"/><path d="M9 17h16M10.5 13h13M10.5 21h13"/></g></svg>
    </li>
  </ul>

  <div class="dot-band" role="img" aria-label="Light grey dotted band along the bottom edge"></div>
</section>

<section class="card card-back" aria-label="Business card, brand side">
  <svg class="shapes" width="767" height="436" viewBox="0 0 767 436">
    <path fill="var(--grey-deep)" d="M0,0 H767 V142 C520,150 260,95 0,0 Z"/>
    <path fill="var(--grey)" d="M55,0 H767 V126 C530,132 280,82 55,0 Z"/>
    <path fill="var(--navy-deep)" d="M0,300 C260,290 560,330 767,420 V436 H0 Z"/>
    <path fill="var(--navy)" d="M0,318 C250,305 520,345 740,436 H0 Z"/>
  </svg>

  <div class="back-brand">
    <div class="mark"></div>
    <p class="brand-name">WARD COMPASS</p>
  </div>
</section>

</body>
</html>
```